Bramblecot Namecard

We have a regular but rotating group of Actors and Directors who meet weekly. I'd like to make a nametag (first and last names) for each of the participants which would fit on a regular business card. The first name would be over-sized to enable reading at a distance. The background & border should project fun and warmth. The Bramblecot is meant to be a place to play without judgement or negative vibes.

```html
<!DOCTYPE html>
<html lang="en">
<head>
<meta charset="utf-8">
<title>Bramblecot Namecard</title>
<link href="https://fonts.googleapis.com/css2?family=Alfa+Slab+One&family=Jost:wght@400&display=swap" rel="stylesheet">
<style>
  :root {
    --sky-teal: #5d807c;
    --sky-haze: #9fae9f;
    --warm-sand: #cdb7a0;
    --dusk-rose: #a9675a;
    --ember: #7a3526;
    --deep-ember: #5c2219;
    --glow-amber: #e2c489;
    --glow-blush: #e7b9a4;
    --badge-fill: rgba(255, 250, 240, 0.28);
    --badge-edge: rgba(255, 250, 240, 0.18);
    --name-ink: #ffffff;
  }
  html, body {
    margin: 0;
    padding: 0;
    width: 1200px;
    height: 686px;
    overflow: hidden;
    background: #ffffff;
  }
  .namecard {
    position: relative;
    width: 1200px;
    height: 686px;
    overflow: hidden;
  }
  .namecard__backdrop {
    position: absolute;
    inset: 0;
    background:
      radial-gradient(circle at 150px 390px, rgba(226,196,137,0.55) 0 40px, transparent 90px),
      radial-gradient(circle at 60px 260px, rgba(226,196,137,0.35) 0 30px, transparent 80px),
      radial-gradient(circle at 1040px 300px, rgba(231,185,164,0.45) 0 40px, transparent 110px),
      radial-gradient(circle at 960px 470px, rgba(231,185,164,0.40) 0 35px, transparent 95px),
      radial-gradient(circle at 1150px 420px, rgba(226,196,137,0.30) 0 30px, transparent 90px),
      radial-gradient(ellipse 60% 35% at 50% 45%, rgba(231,214,190,0.55), transparent 75%),
      radial-gradient(ellipse 45% 45% at 0% 100%, var(--deep-ember), transparent 80%),
      radial-gradient(ellipse 50% 40% at 100% 100%, var(--dusk-rose), transparent 80%),
      linear-gradient(180deg,
        var(--sky-teal) 0%,
        var(--sky-haze) 18%,
        var(--warm-sand) 40%,
        #b98a73 62%,
        var(--dusk-rose) 80%,
        var(--ember) 100%);
  }
  .namecard__badge {
    position: absolute;
    left: 0;
    top: 0;
    width: 1200px;
    height: 686px;
  }
  .badge__disc {
    fill: var(--badge-fill);
  }
  .badge__first-name {
    font-family: "Alfa Slab One", serif;
    font-size: 250px;
    fill: var(--name-ink);
  }
  .badge__last-name {
    font-family: "Jost", sans-serif;
    font-size: 31px;
    font-weight: 400;
    fill: var(--name-ink);
  }
</style>
</head>
<body>
  <main class="namecard">
    <div class="namecard__backdrop" role="img" aria-label="Soft blurred bokeh of warm evening lights, teal sky fading into amber and rose"></div>
    <svg class="namecard__badge" viewBox="0 0 1200 686" xmlns="http://www.w3.org/2000/svg">
      <defs>
        <linearGradient id="discShade" x1="0" y1="0" x2="0" y2="1">
          <stop offset="0" stop-color="#fffaf0" stop-opacity="0.30"/>
          <stop offset="0.5" stop-color="#fffaf0" stop-opacity="0.30"/>
          <stop offset="1" stop-color="#fffaf0" stop-opacity="0.22"/>
        </linearGradient>
      </defs>
      <circle class="badge__disc" cx="576" cy="325" r="312" fill="url(#discShade)"/>
      <text class="badge__first-name" x="406" y="389" textLength="357" lengthAdjust="spacingAndGlyphs">Mark</text>
      <text class="badge__last-name" x="414" y="451" textLength="336" lengthAdjust="spacing">HOLLINS</text>
    </svg>
  </main>
</body>
</html>
```